Brightleaf Dentistry - Flyer - Modern & Eye catching campaign flyer

Need front & back side full page flyer designs for both 1) Grand opening 2) On-going campaign.

Attached the new dental office logo.
Attached our other dental clinic flyer designs for content.

Target Market(s)

Cosmetic dentistry

Industry/Entity Type

Health Care

Requirements
Must have
• decent, modern and eye catching marketing flyers.
Nice to have
• - Nice space
• - Highlight phone number
• - Highlight special features like convenient hours, call or text, for all ages, digital facility, etc
Should not have
• - Don't want to fill the flyer with too much wordings
• - Too many colors

```html
<!DOCTYPE html>
<html lang="en">
<head>
<meta charset="utf-8">
<title>Brightleaf Dentistry – Grand Opening Postcard</title>
<link href="https://fonts.googleapis.com/css2?family=Montserrat:wght@400;500;600;700;800&family=Oswald:wght@700&display=swap" rel="stylesheet">
<style>
:root{
  --navy:#2b3f5c;
  --navy-dark:#1f2e45;
  --cyan:#1ba8d9;
  --orange:#f08a24;
  --white:#ffffff;
  --ink:#2b3f5c;
  --bg:#5b5c5e;
  --rule:#b9bfc7;
}
*{box-sizing:border-box;margin:0;padding:0}
html,body{width:1200px;height:912px;overflow:hidden}
body{background:var(--bg);font-family:"Montserrat",sans-serif;color:var(--ink);position:relative}
.card{position:absolute;left:270px;width:660px;height:440px;background:var(--white);overflow:hidden;box-shadow:0 6px 18px rgba(0,0,0,.35)}
.card--front{top:12px}
.card--back{top:462px}
.card svg.shapes{position:absolute;inset:0}
.abs{position:absolute}

/* front */
.headline{left:28px;top:18px;font-family:"Oswald",sans-serif;font-size:36px;letter-spacing:.5px;color:var(--navy);text-transform:uppercase}
.invite-band{left:0;top:70px;width:340px;height:50px;background:var(--cyan);color:var(--white);font-weight:800;font-size:15px;line-height:19px;text-transform:uppercase;padding:6px 0 0 32px;letter-spacing:.6px}
.event-date{left:28px;top:132px;display:flex;gap:10px;align-items:center}
.event-date .when{color:var(--orange);font-weight:800;font-size:15px;line-height:17px;text-transform:uppercase}
.event-date .when small{display:block;font-size:12px;font-weight:700}
.event-extras{left:28px;top:176px;font-size:11.5px;font-weight:600;line-height:15px}
.event-extras .tagline{text-transform:uppercase;font-weight:500;letter-spacing:.3px}
.call-title{left:28px;top:232px;font-size:19px;font-weight:800}
.phone-pill{display:flex;align-items:center;height:30px;background:var(--cyan);border-radius:0 15px 15px 0;color:var(--white);font-weight:800;letter-spacing:1px}
.phone-pill .icon{width:34px;height:30px;background:var(--navy);border-radius:15px 0 0 15px;display:flex;align-items:center;justify-content:center}
.front-phone{left:28px;top:262px;width:230px;font-size:21px}
.front-phone span{padding-left:14px}
.hours{font-size:11px;font-weight:700;color:var(--navy)}
.front-hours{left:28px;top:297px}
.fineprint{left:28px;top:314px;font-size:8px;font-weight:500}
.patients{left:28px;top:374px;color:var(--cyan);font-weight:800;font-size:13px}
.contacts{left:28px;top:394px;display:flex;flex-direction:column;gap:3px;color:var(--white);font-size:10.5px;font-weight:500}
.contacts span{display:flex;align-items:center;gap:6px}
.brand-front{right:22px;bottom:20px;display:flex;align-items:center;gap:8px;color:var(--white);font-weight:700;font-size:21px;letter-spacing:.5px}
.brand-dot{width:16px;height:16px;border-radius:50%;background:var(--cyan)}

/* back */
.insurance-band{left:0;top:14px;width:300px;height:26px;background:var(--navy);color:var(--white);font-weight:800;font-size:14px;padding:4px 0 0 22px;text-transform:uppercase}
.insurance-band b{color:var(--cyan)}
.service-title{left:22px;top:48px;font-size:15px;font-weight:800;text-transform:uppercase;letter-spacing:.5px}
.features{left:22px;top:70px;list-style:none;font-size:11.5px;font-weight:700;line-height:16px}
.features li{display:flex;gap:6px;align-items:flex-start}
.features li svg{flex:none;margin-top:3px}
.features .detail{font-weight:500}
.fun{left:22px;top:216px;font-size:12.5px;font-weight:800;border-bottom:1.5px dotted var(--navy);width:210px;padding-bottom:2px}
.offers{left:22px;top:240px;list-style:none;display:flex;flex-direction:column;gap:5px}
.offer{display:flex;align-items:center;width:260px;height:19px;border:1.5px solid var(--orange);border-radius:0 10px 10px 0;font-size:10.5px;font-weight:600}
.offer .tag{background:var(--orange);color:var(--white);font-weight:800;font-size:11px;height:100%;width:62px;display:flex;align-items:center;padding-left:7px;margin-right:10px}
.back-phone{left:22px;top:366px;width:250px;font-size:23px}
.back-phone span{padding-left:16px}
.back-hours{left:22px;top:404px;color:var(--cyan);font-size:12px;font-weight:700}
.brand-back{left:372px;top:44px;display:flex;align-items:center;gap:8px;color:var(--cyan);font-weight:700;font-size:21px}
.address{left:372px;top:80px;font-size:11.5px;font-weight:500;line-height:15px;font-style:normal}
.stamp{left:556px;top:68px;width:80px;height:62px;border:1.5px solid var(--rule)}
.address-line{position:absolute;left:372px;width:262px;height:1px;background:var(--rule)}
.map{left:372px;top:302px;width:262px;height:116px;border:5px solid var(--cyan);border-radius:12px;background:linear-gradient(135deg,#eceef0,#dfe3e7)}
</style>
</head>
<body>

<section class="card card--front" aria-label="Grand opening postcard, front">
  <svg class="shapes" viewBox="0 0 660 440">
    <defs>
      <linearGradient id="familyTone" x1="0" y1="0" x2="0" y2="1">
        <stop offset="0" stop-color="#e9f3f8"/>
        <stop offset=".45" stop-color="#c9a58c"/>
        <stop offset="1" stop-color="#1e2c44"/>
      </linearGradient>
    </defs>
    <path d="M0 368 H336 C332 395 338 420 350 440 H0 Z" fill="var(--navy)"/>
    <path role="img" aria-label="Photo of a smiling family giving thumbs up, with party balloons above" d="M408 0 H660 V440 H362 C300 360 300 120 408 0 Z" fill="url(#familyTone)"/>
    <path d="M398 0 C290 120 290 360 352 440" fill="none" stroke="var(--cyan)" stroke-width="10"/>
  </svg>

  <h1 class="abs headline">Grand Opening</h1>
  <div class="abs invite-band">You are invited to<br>open house party!</div>

  <div class="abs event-date">
    <svg width="30" height="28" viewBox="0 0 30 28" aria-hidden="true">
      <rect x="2" y="5" width="24" height="21" rx="2" fill="none" stroke="var(--navy)" stroke-width="2"/>
      <line x1="2" y1="11" x2="26" y2="11" stroke="var(--navy)" stroke-width="2"/>
      <line x1="8" y1="2" x2="8" y2="7" stroke="var(--navy)" stroke-width="2"/>
      <line x1="20" y1="2" x2="20" y2="7" stroke="var(--navy)" stroke-width="2"/>
      <circle cx="23" cy="21" r="6" fill="var(--white)" stroke="var(--navy)" stroke-width="2"/>
    </svg>
    <p class="when">June 22nd, 2019<small>Saturday, 2 - 6 PM</small></p>
  </div>

  <div class="abs event-extras">
    <p>Pizza | Drinks | Raffle (tablet, etc)</p>
    <p>Face Painting &amp; Balloons</p>
    <p class="tagline">We can't wait to meet you!</p>
  </div>

  <p class="abs call-title">Call or Text Us Now:</p>
  <div class="abs phone-pill front-phone">
    <span class="icon"><svg width="16" height="16" viewBox="0 0 24 24" aria-hidden="true"><path d="M6.6 10.8a15 15 0 0 0 6.6 6.6l2.2-2.2a1 1 0 0 1 1-.25 11.4 11.4 0 0 0 3.6.57 1 1 0 0 1 1 1V20a1 1 0 0 1-1 1A17 17 0 0 1 3 4a1 1 0 0 1 1-1h3.5a1 1 0 0 1 1 1c0 1.25.2 2.45.57 3.6a1 1 0 0 1-.25 1z" fill="#fff"/></svg></span>
    <span>610.555.0187</span>
  </div>
  <p class="abs hours front-hours">Convenient Evening &amp; Saturday Hours</p>
  <p class="abs fineprint">* Offers cannot be combined and valid for 30 days. Call for details.</p>

  <p class="abs patients">Now accepting NEW PATIENTS!</p>
  <div class="abs contacts">
    <span><svg width="12" height="10" viewBox="0 0 12 10" aria-hidden="true"><rect x=".5" y=".5" width="11" height="9" rx="1" fill="none" stroke="var(--cyan)"/><path d="M1 1l5 4 5-4" fill="none" stroke="var(--cyan)"/></svg>info@brightleafdental.com</span>
    <span><svg width="12" height="12" viewBox="0 0 12 12" aria-hidden="true"><circle cx="6" cy="6" r="5.5" fill="none" stroke="var(--cyan)"/><ellipse cx="6" cy="6" rx="2.5" ry="5.5" fill="none" stroke="var(--cyan)"/><line x1=".5" y1="6" x2="11.5" y2="6" stroke="var(--cyan)"/></svg>www.brightleafdental.com</span>
  </div>

  <div class="abs brand-front"><span class="brand-dot"></span>Brightleaf Dentistry</div>
</section>

<section class="card card--back" aria-label="Grand opening postcard, back">
  <svg class="shapes" viewBox="0 0 660 440">
    <path d="M0 356 H288 C270 390 262 415 260 440 H0 Z" fill="var(--navy)"/>
    <path d="M300 14 C400 110 390 300 262 440" fill="none" stroke="var(--cyan)" stroke-width="9"/>
    <circle cx="322" cy="186" r="60" fill="var(--navy)"/>
    <circle role="img" aria-label="Photo of a dentist and a smiling patient in the dental chair" cx="322" cy="186" r="55" fill="#d9e6ee" stroke="var(--white)" stroke-width="3"/>
  </svg>

  <div class="abs insurance-band">Major Insurances <b>Accepted</b></div>
  <h2 class="abs service-title">Cosmetic &amp; Family Dentistry</h2>
  <ul class="abs features">
    <li><svg width="9" height="9" viewBox="0 0 10 10"><rect x=".5" y=".5" width="9" height="9" fill="none" stroke="var(--cyan)"/><path d="M2 5l2 2 4-5" fill="none" stroke="var(--cyan)" stroke-width="1.5"/></svg>Same-day Appointments</li>
    <li><svg width="9" height="9" viewBox="0 0 10 10"><rect x=".5" y=".5" width="9" height="9" fill="none" stroke="var(--cyan)"/><path d="M2 5l2 2 4-5" fill="none" stroke="var(--cyan)" stroke-width="1.5"/></svg>* After Hours Support</li>
    <li><svg width="9" height="9" viewBox="0 0 10 10"><rect x=".5" y=".5" width="9" height="9" fill="none" stroke="var(--cyan)"/><path d="M2 5l2 2 4-5" fill="none" stroke="var(--cyan)" stroke-width="1.5"/></svg>State-Of-The-Art Equipment</li>
    <li><svg width="9" height="9" viewBox="0 0 10 10"><rect x=".5" y=".5" width="9" height="9" fill="none" stroke="var(--cyan)"/><path d="M2 5l2 2 4-5" fill="none" stroke="var(--cyan)" stroke-width="1.5"/></svg>Kids &amp; Teens Friendly Staff</li>
    <li><svg width="9" height="9" viewBox="0 0 10 10"><rect x=".5" y=".5" width="9" height="9" fill="none" stroke="var(--cyan)"/><path d="M2 5l2 2 4-5" fill="none" stroke="var(--cyan)" stroke-width="1.5"/></svg><span>Relax &amp; Unwind:<br><span class="detail">Massage chairs, Coffee station,<br>tablets, Kids corner, 4k TVs,<br>speakers, sound system, etc.</span></span></li>
  </ul>
  <p class="abs fun">Dental visits can be fun!</p>
  <ul class="abs offers">
    <li class="offer"><span class="tag">$150 off</span>Treatment plan</li>
    <li class="offer"><span class="tag">$400 off</span>1st Implant &amp; ClearAlign</li>
    <li class="offer"><span class="tag">$59</span>Exam, X-Rays &amp; Cleaning</li>
    <li class="offer"><span class="tag">FREE</span>Whitening kit for 1st 100 patients</li>
  </ul>
  <div class="abs phone-pill back-phone">
    <span class="icon"><svg width="16" height="16" viewBox="0 0 24 24" aria-hidden="true"><path d="M6.6 10.8a15 15 0 0 0 6.6 6.6l2.2-2.2a1 1 0 0 1 1-.25 11.4 11.4 0 0 0 3.6.57 1 1 0 0 1 1 1V20a1 1 0 0 1-1 1A17 17 0 0 1 3 4a1 1 0 0 1 1-1h3.5a1 1 0 0 1 1 1c0 1.25.2 2.45.57 3.6a1 1 0 0 1-.25 1z" fill="#fff"/></svg></span>
    <span>610.555.0187</span>
  </div>
  <p class="abs back-hours">Convenient Evening &amp; Saturday Hours</p>

  <div class="abs brand-back"><span class="brand-dot"></span>Brightleaf Dentistry</div>
  <address class="abs address">1480 Alder Rd,<br>Maple Hill PA 19000</address>
  <div class="abs stamp" aria-label="Stamp area"></div>
  <span class="address-line" style="top:180px"></span>
  <span class="address-line" style="top:222px"></span>
  <span class="address-line" style="top:264px"></span>
  <div class="abs map" role="img" aria-label="Street map showing the office location"></div>
</section>

</body>
</html>
```